Varnel Group Limited Stationary

We are in need of business card and letterhead designs. We are looking for clean modern designs that complement the style and feel of our logo.

```html
<!DOCTYPE html>
<html lang="en">
<head>
<meta charset="utf-8">
<title>Varnel Group Limited – Stationery</title>
<link rel="stylesheet" href="https://fonts.googleapis.com/css2?family=Open+Sans:wght@400;600;700&display=swap">
<style>
  :root {
    --bg: #e4e5e7;
    --paper: #ffffff;
    --navy: #27407f;
    --charcoal: #3b3e44;
    --ink: #3a3a3a;
    --soft: #8a93ad;
    --window: #d9d9dc;
    --shadow: 0 6px 18px rgba(0,0,0,.18);
  }
  * { box-sizing: border-box; margin: 0; padding: 0; }
  html, body { width: 1200px; height: 900px; overflow: hidden; }
  body {
    background: var(--bg);
    font-family: "Open Sans", Arial, sans-serif;
    color: var(--ink);
    position: relative;
  }
  .sheet {
    position: absolute;
    background: var(--paper);
    box-shadow: var(--shadow);
    overflow: hidden;
  }
  .brand { display: flex; align-items: center; gap: 8px; }
  .brand-dot { border-radius: 50%; background: var(--navy); flex: none; }
  .brand-name { color: var(--navy); font-weight: 600; letter-spacing: .02em; }
  .edge-band { position: absolute; left: 0; bottom: 0; width: 100%; display: block; }
  .faint-circle {
    position: absolute; border-radius: 50%;
    background: var(--soft); opacity: .18;
  }

  /* Letterhead */
  .letterhead { left: 70px; top: 40px; width: 470px; height: 665px; }
  .letterhead .brand { position: absolute; left: 34px; top: 34px; }
  .letterhead .brand-dot { width: 26px; height: 26px; }
  .letterhead .brand-name { font-size: 19px; }
  .letterhead .brand-rule { position: absolute; left: 34px; top: 70px; width: 150px; height: 1px; background: var(--soft); }
  .greeting { position: absolute; left: 34px; top: 92px; font-size: 9px; }
  .sender {
    position: absolute; right: 30px; top: 118px; text-align: right;
    font-size: 7.5px; line-height: 1.45;
  }
  .sender .company { color: var(--navy); font-weight: 700; font-size: 10px; margin-bottom: 3px; }
  .sender .label { color: var(--navy); font-weight: 700; margin-top: 3px; }
  .letter-body {
    position: absolute; left: 34px; top: 118px; width: 300px;
    font-size: 7.5px; line-height: 1.6; text-align: left;
  }
  .letter-body p { margin-bottom: 9px; text-indent: 26px; }
  .letterhead .faint-circle { width: 300px; height: 300px; left: 140px; top: 330px; }

  /* Cards */
  .card { width: 300px; height: 170px; }
  .card-front { left: 620px; top: 55px; }
  .card-front .brand { position: absolute; left: 0; right: 0; top: 62px; justify-content: center; }
  .card-front .brand-dot { width: 22px; height: 22px; }
  .card-front .brand-name { font-size: 17px; }
  .card-front .web { position: absolute; left: 0; right: 0; top: 100px; text-align: center; font-size: 7.5px; }

  .card-back { left: 860px; top: 250px; }
  .card-back .brand { position: absolute; left: 18px; top: 16px; }
  .card-back .brand-dot { width: 16px; height: 16px; }
  .card-back .brand-name { font-size: 12px; }
  .card-back .contacts { position: absolute; left: 18px; top: 50px; font-size: 7px; line-height: 1.7; list-style: none; }
  .contacts li { display: flex; align-items: center; gap: 5px; }
  .contacts svg { width: 7px; height: 7px; fill: var(--navy); flex: none; }
  .card-back .person { position: absolute; right: 18px; top: 48px; text-align: right; font-size: 7px; line-height: 1.5; }
  .person .name { color: var(--navy); font-weight: 700; font-size: 13px; letter-spacing: .04em; }
  .person .role { margin-bottom: 5px; }
  .person .label { color: var(--navy); font-weight: 700; }

  /* Envelope */
  .envelope { left: 580px; top: 475px; width: 560px; height: 290px; }
  .envelope .brand { position: absolute; left: 30px; top: 26px; }
  .envelope .brand-dot { width: 24px; height: 24px; }
  .envelope .brand-name { font-size: 18px; }
  .envelope .sender-block { position: absolute; left: 30px; top: 66px; font-size: 7.5px; line-height: 1.5; }
  .sender-block .company { color: var(--navy); font-weight: 700; font-size: 10px; margin-bottom: 3px; }
  .sender-block .label { color: var(--navy); font-weight: 700; margin-top: 3px; }
  .envelope .address-window { position: absolute; right: 40px; top: 120px; width: 220px; height: 90px; background: var(--window); }
  .envelope .faint-circle { width: 200px; height: 200px; right: -30px; top: 150px; }
</style>
</head>
<body>

<!-- Letterhead -->
<section class="sheet letterhead">
  <div class="faint-circle"></div>
  <div class="brand"><span class="brand-dot"></span><span class="brand-name">Varnel Group</span></div>
  <div class="brand-rule"></div>
  <p class="greeting">HELLO!</p>
  <div class="sender">
    <p class="company">VARNEL GROUP LIMITED</p>
    <p>0400 1122 334</p>
    <p>hello@varnel.net.au</p>
    <p>www.varnelgroup.com</p>
    <p class="label">ADDRESS:</p>
    <p>Level 12, 88 Harbour Street</p>
    <p>Perth WA 6000</p>
    <p>Phone: (08) 9100 2045</p>
  </div>
  <div class="letter-body">
    <p>Contrary to popular belief, Lorem Ipsum is not simply random text. It has roots in a piece of classical Latin literature from 45 BC, making it over 2000 years old. A Latin professor looked up one of the more obscure Latin words and, going through the cites of the word in classical literature, discovered the undoubtable source. The first line comes from a line in section 1.10.32.</p>
    <p>The standard chunk of Lorem Ipsum used since the 1500s is reproduced below for those interested. Sections 1.10.32 and 1.10.33 are also reproduced in their exact original form, accompanied by English versions.</p>
    <p>Contrary to popular belief, Lorem Ipsum is not simply random text. It has roots in a piece of classical Latin literature from 45 BC, making it over 2000 years old. A Latin professor looked up one of the more obscure Latin words and, going through the cites of the word in classical literature, discovered the undoubtable source. The first line comes from a line in section 1.10.32.</p>
    <p>The standard chunk of Lorem Ipsum used since the 1500s is reproduced below for those interested. Sections 1.10.32 and 1.10.33 are also reproduced in their exact original form, accompanied by English versions.</p>
  </div>
  <svg class="edge-band" viewBox="0 0 470 34" height="34" preserveAspectRatio="none" aria-hidden="true">
    <rect x="0" y="22" width="470" height="12" fill="var(--navy)"/>
    <polygon points="300,34 318,12 330,12 312,34" fill="var(--navy)"/>
    <polygon points="322,34 340,12 352,12 334,34" fill="var(--navy)"/>
    <polygon points="344,34 362,0 470,0 470,34" fill="var(--charcoal)"/>
    <polygon points="332,34 352,22 358,22 338,34" fill="#fff"/>
  </svg>
</section>

<!-- Business card, front -->
<section class="sheet card card-front">
  <div class="brand"><span class="brand-dot"></span><span class="brand-name">Varnel Group</span></div>
  <p class="web">www.varnelgroup.com</p>
</section>

<!-- Business card, back -->
<section class="sheet card card-back">
  <div class="brand"><span class="brand-dot"></span><span class="brand-name">Varnel Group</span></div>
  <ul class="contacts">
    <li><svg viewBox="0 0 10 10"><rect x="2.5" y="0" width="5" height="10" rx="1"/></svg>0400 1122 334</li>
    <li><svg viewBox="0 0 10 10"><path d="M3 0h2l1 3-1.5 1a6 6 0 0 0 1.5 2l1-1.5 3 1v2c0 1-1 2-2 2A8 8 0 0 1 0 3c0-1 1-3 3-3z"/></svg>0400 1122 335</li>
    <li><svg viewBox="0 0 10 10"><path d="M0 2h10v6H0z M0 2l5 4 5-4" /></svg>hello@varnel.net.au</li>
    <li><svg viewBox="0 0 10 10"><circle cx="5" cy="5" r="5"/></svg>www.varnelgroup.com</li>
  </ul>
  <div class="person">
    <p class="name">JOHN DOE</p>
    <p class="role">General Director</p>
    <p class="label">ADDRESS:</p>
    <p>Level 12, 88 Harbour Street</p>
    <p>Perth WA 6000</p>
    <p>Phone: (08) 9100 2045</p>
  </div>
  <svg class="edge-band" viewBox="0 0 300 18" height="18" preserveAspectRatio="none" aria-hidden="true">
    <rect x="0" y="8" width="300" height="10" fill="var(--navy)"/>
    <polygon points="200,18 212,4 220,4 208,18" fill="var(--navy)"/>
    <polygon points="222,18 236,0 300,0 300,18" fill="var(--charcoal)"/>
  </svg>
</section>

<!-- Envelope -->
<section class="sheet envelope">
  <div class="faint-circle"></div>
  <div class="brand"><span class="brand-dot"></span><span class="brand-name">Varnel Group</span></div>
  <div class="sender-block">
    <p class="company">VARNEL GROUP LIMITED</p>
    <p>0400 1122 334</p>
    <p>hello@varnel.net.au</p>
    <p>www.varnelgroup.com</p>
    <p class="label">ADDRESS:</p>
    <p>Level 12, 88 Harbour Street</p>
    <p>Perth WA 6000</p>
    <p>Phone: (08) 9100 2045</p>
  </div>
  <div class="address-window"></div>
  <svg class="edge-band" viewBox="0 0 560 26" height="26" preserveAspectRatio="none" aria-hidden="true">
    <rect x="0" y="16" width="560" height="10" fill="var(--navy)"/>
    <polygon points="410,26 426,8 436,8 420,26" fill="var(--navy)"/>
    <polygon points="440,26 462,0 560,0 560,26" fill="var(--charcoal)"/>
  </svg>
</section>

</body>
</html>
```